Flyer für eine Imkerei
Wunderbare unkomplizierte Zusammenarbeit mit einem tollen Designer. Extrem gutes Verständnis der Grundidee, super flexibles einarbeiten eigener Verbesserungsvorschläge - einfach sehr kompetent! Danke dafür.
Zielgruppe
Ich bin Hobbyimker mit einer sehr kleinen Imkerei im Dorf. Ich biete lokalen Honig an. Der Flyer soll ein Infoflyer für Kunden und evt. Neukunden sein.
Aufgabenstellung
Bitte im Wickelfalz hochkant A4, (gefaltet also 99x210). Textbausteine sind als Datei angehängt. Bitte nur den Text nutzen, nicht Schriftgröße, Schritart etc. Ebenso ist eigenes Bildmaterial vorhanden. Ich würde mich über ein edles aber schlicht modernes Design freuen. Das Design darf gern Honigwaben (Hexagon) als Grundidee beinhalten. Bevorzugte Farbtöne sind schwarz, gold, gelb, orange (honigfarben) bis Weinrot (siehe Honigetikett auf dem Foto).

```html
<!DOCTYPE html>
<html lang="de">
<head>
<meta charset="utf-8">
<title>Flyer Imkerei Saaletal</title>
<link rel="stylesheet" href="https://fonts.googleapis.com/css2?family=Merriweather:ital,wght@0,400;0,700;0,900;1,700;1,900&family=Source+Serif+4:ital,wght@0,400;0,600;1,400&family=Parisienne&display=swap">
<style>
:root{
  --stage:#7b808a;
  --paper:#ffffff;
  --honey:#e3a81f;
  --forest:#2f5128;
  --ink:#3a2f28;
  --photo-wood:#b08a52;
}
*{box-sizing:border-box;margin:0;padding:0}
html,body{width:845px;height:1200px;overflow:hidden}
body{background:var(--stage);position:relative;font-family:"Source Serif 4",Georgia,serif;color:var(--ink)}
.sheet{position:absolute;left:86px;width:684px;height:484px;background:var(--paper);overflow:hidden}
.sheet--outside{top:74px}
.sheet--inside{top:633px}
.abs{position:absolute}
.fill{position:absolute}
.h-panel{font-family:"Merriweather",Georgia,serif;font-weight:700;color:var(--forest);font-size:12px;line-height:1.3;white-space:nowrap}
.body{font-size:8px;line-height:12.2px;white-space:nowrap}
.title{font-family:"Merriweather",Georgia,serif;font-weight:900;font-size:25px;line-height:29px;color:var(--honey)}
.honeycomb{background:linear-gradient(135deg,#e9b532,#dc9e14)}
.honeycomb--soft{background:linear-gradient(135deg,rgba(227,168,31,.85),rgba(227,168,31,.55))}
.sketch{background:#d9c6b4;border-radius:50%}
.frame{border:3px solid var(--honey)}
.center{text-align:center}
.script{font-family:"Parisienne",cursive;color:var(--forest);font-size:13px;line-height:16px}
.list-h{font-family:"Merriweather",Georgia,serif;font-weight:700;color:var(--forest);font-size:11px;line-height:16px;white-space:nowrap}
</style>
</head>
<body>

<section class="sheet sheet--outside">
  <!-- Panel: Über uns -->
  <div class="fill" role="img" aria-label="Foto: Bienenstöcke auf einer sonnigen Waldwiese" style="left:0;top:0;width:224px;height:158px;background:linear-gradient(180deg,#6f9a3e 0%,#3f6e2a 45%,var(--photo-wood) 60%,#4d7a2c 100%)"></div>
  <h2 class="h-panel abs" style="left:31px;top:168px">Über uns</h2>
  <div class="fill sketch" role="img" aria-label="Zeichnung eines Honiglöffels" style="left:100px;top:163px;width:30px;height:24px"></div>
  <p class="abs" style="left:31px;top:187px;font-family:Merriweather,serif;font-style:italic;font-weight:700;font-size:7.4px;line-height:12.2px;color:var(--forest);white-space:nowrap">Herzlich willkommen in unserer kleinen<br>Hobbyimkerei im schönen Saaletal!</p>
  <p class="abs body" style="left:31px;top:215px">Bei uns erhalten Sie alles aus einer Hand.<br>Von der sorgsamen Pflege der sensiblen<br>Bienenvölker über die Honigernte bis hin<br>zum fertig etikettierten Glas wird jeder<br>Arbeitsschritt persönlich vor Ort mit<br>größter Sorgfalt ausgeführt, um ein reines<br>und unverfälschtes Naturprodukt<br>zu garantieren.</p>
  <div class="fill honeycomb" role="img" aria-label="Wabenmuster am Rand" style="left:0;top:308px;width:28px;height:137px;opacity:.9"></div>
  <h2 class="h-panel abs" style="left:31px;top:316px">Natürlich &amp; schonend</h2>
  <div class="fill sketch" role="img" aria-label="Zeichnung einer Blüte" style="left:162px;top:322px;width:38px;height:36px"></div>
  <p class="abs body" style="left:31px;top:335px">Wir betreiben eine sanfte und<br>wesensgemäße Bienenhaltung. Die<br>Bienenstöcke haben einen festen Standort<br>auf einer sonnigen Waldlichtung.<br>Sie werden im Saisonverlauf nicht<br>transportiert, sondern sammeln den Nektar<br>der Pflanzen, die hier im Saaletal ganz<br>natürlich saisonal blühen. Das garantiert<br>einen authentischen Honig aus unserer<br>Heimat.</p>

  <!-- Panel: Probieren -->
  <div class="fill honeycomb--soft" role="img" aria-label="Wabenmuster mit gezeichnetem Honigglas" style="left:224px;top:0;width:228px;height:79px"></div>
  <h2 class="h-panel abs" style="left:245px;top:88px">Probieren Sie selbst!</h2>
  <p class="abs body center" style="left:225px;top:108px;width:228px">Wurde Ihre Neugier geweckt? Dann freuen wir<br>uns, wenn Sie den reinen Geschmack unseres<br>lokalen Produktes probieren möchten. Unser<br>Honig ist vor Ort erhältlich.</p>
  <p class="abs body center" style="left:225px;top:169px;width:228px">Für Bestellungen und Abholungen<br>erreichen Sie uns unter:</p>
  <p class="abs center" style="left:225px;top:200px;width:228px;font-family:Merriweather,serif;font-weight:700;font-size:14px;color:var(--forest)">Telefonnummer</p>
  <div class="fill" role="img" aria-label="Foto: Wabenrahmen mit verdeckeltem Honig" style="left:225px;top:244px;width:112px;height:106px;background:linear-gradient(135deg,#5a4a2e,#d79a2a 45%,#b47a1c)"></div>
  <div class="fill" role="img" aria-label="Foto: Bienen auf einem Rähmchen" style="left:340px;top:244px;width:113px;height:106px;background:linear-gradient(135deg,#3a3026,#c9b08a 55%,#4a3c2c)"></div>
  <div class="fill sketch" role="img" aria-label="Zeichnung einer Blüte" style="left:326px;top:362px;width:28px;height:28px"></div>
  <p class="abs script center" style="left:225px;top:404px;width:228px">Schauen Sie gern vorbei.<br>Wir freuen uns auf Sie!</p>

  <!-- Panel: Titel -->
  <h1 class="abs title" style="left:477px;top:54px">Feinster<br>Honig<br>aus dem<br>Saaletal</h1>
  <div class="fill sketch" role="img" aria-label="Zeichnung von Blüten" style="left:594px;top:160px;width:60px;height:40px"></div>
  <div class="fill honeycomb" role="img" aria-label="Wabenmuster mit gezeichneten Blüten und Bienen" style="left:552px;top:180px;width:132px;height:134px;clip-path:polygon(30% 0,100% 0,100% 100%,25% 100%,0 55%)"></div>
  <div class="fill sketch" role="img" aria-label="Zeichnung einer Biene" style="left:510px;top:232px;width:36px;height:38px"></div>
  <div class="fill sketch" role="img" aria-label="Zeichnung einer Biene" style="left:590px;top:341px;width:46px;height:32px"></div>
  <p class="abs" style="left:485px;top:397px;font-family:Merriweather,serif;font-style:italic;font-weight:700;font-size:10.5px;letter-spacing:.8px;color:var(--forest);white-space:nowrap">Natürlich, Regional &amp; Direkt</p>
  <div class="abs" style="left:518px;top:424px;width:100px;border-top:3px dotted var(--honey)"></div>
  <p class="abs" style="left:478px;top:446px;font-family:Merriweather,serif;font-weight:700;font-size:7.6px;letter-spacing:1px;color:var(--forest)">Name Ort Straße</p>
</section>

<section class="sheet sheet--inside">
  <!-- Panel: Unser Honig -->
  <h2 class="abs title" style="left:31px;top:22px;font-size:26px;line-height:28px">Unser<br>Honig</h2>
  <div class="fill honeycomb" role="img" aria-label="Wabenmuster mit gezeichneter Biene" style="left:150px;top:0;width:82px;height:88px;clip-path:polygon(20% 0,100% 0,100% 100%,50% 100%,0 65%)"></div>
  <p class="abs body" style="left:31px;top:91px">Durch den festen Standort können mit zwei<br>Honigernten im Jahr folgende Sorten angeboten<br>werden, die den Geschmack der Saison<br>einfangen:</p>
  <h3 class="h-panel abs" style="left:31px;top:144px;line-height:17px">Frühtracht –<br>cremig:</h3>
  <div class="fill frame" role="img" aria-label="Foto: Biene auf gelber Frühlingsblüte" style="left:116px;top:157px;width:114px;height:92px;background:linear-gradient(135deg,#2f4a1c,#f0d12a 50%,#6a8a22);clip-path:polygon(0 0,100% 0,100% 100%,10% 100%,0 85%)"></div>
  <p class="abs body" style="left:31px;top:181px">Gesammelt von den<br>ersten Blüten des<br>Jahres - vorwiegend<br>Obstblüte und Raps.<br>Für eine streichzarte<br>Konsistenz wird<br>dieser milde, blumige<br>Honig vor dem Abfüllen fein-cremig gerührt.</p>
  <h3 class="h-panel abs" style="left:31px;top:281px;line-height:17px">Sommerblüte –<br>flüssig &amp; cremig:</h3>
  <p class="abs body" style="left:31px;top:318px">Ein etwas kräftigerer und aromatischer<br>Honig aus den Blüten des Hochsommers –<br>vorwiegend Linde. Diesen Honig gibt es je<br>nach Verfügbarkeit als flüssige Variante oder<br>ebenfalls fein-cremig gerührt.</p>
  <p class="abs body" style="left:31px;top:384px">Gut zu wissen: Echter Honig kann<br>kristallisieren. Das ist ein natürlicher Prozess<br>und ein Zeichen für hohe Qualität. Im<br>Wasserbad bei maximal 40°C wird er schonend<br>wieder flüssig. Honig bitte kühl, trocken und<br>dunkel lagern.</p>

  <!-- Panel: Warum regional -->
  <h2 class="abs" style="left:253px;top:25px;font-family:Merriweather,serif;font-weight:900;font-size:22px;line-height:26px;color:var(--forest)">Warum<br>regional?</h2>
  <div class="fill sketch" role="img" aria-label="Zeichnung einer Biene" style="left:374px;top:36px;width:40px;height:40px"></div>
  <p class="abs" style="left:253px;top:88px;font-family:Merriweather,serif;font-style:italic;font-weight:900;font-size:20.5px;line-height:26px;color:var(--honey);white-space:nowrap">Gutes für Sie und<br>unsere Heimat</p>
  <h3 class="list-h abs" style="left:255px;top:152px">1.&nbsp; Für die Natur vor unserer<br>Haustür</h3>
  <p class="abs body" style="left:255px;top:190px">Unsere Bienen bestäuben unzählige Pflanzen<br>im Saaletal und sorgen so für den Erhalt der<br>Artenvielfalt.</p>
  <h3 class="list-h abs" style="left:255px;top:229px">2.&nbsp; Absolute Transparenz</h3>
  <p class="abs body" style="left:255px;top:249px">Keine langen Transportwege, keine<br>undurchsichtigen Lieferketten. Der Honig kommt<br>direkt vom Bienenstock im Wald in Ihr Glas. Der<br>Erlös kommt zu 100% unserer Imkerei zugute.</p>
  <h3 class="list-h abs" style="left:255px;top:300px">3. Der Geschmack der Heimat</h3>
  <p class="abs body" style="left:255px;top:320px">Jeder Löffel fängt den einzigartigen<br>Geschmack der vielfältigen lokalen<br>Pflanzenwelt des Saaletals ein.</p>
  <h3 class="list-h abs" style="left:255px;top:359px">4. Geprüfte Qualität</h3>
  <p class="abs body" style="left:255px;top:379px">Unser Honig wird regelmäßig in<br>einem Fachlabor auf Qualität und<br>Zusammensetzung untersucht. Die Analyse<br>der Pollen bestätigt dabei die botanische<br>und geografische Herkunft – eine Garantie<br>für echten Honig aus der Region.</p>

  <!-- Panel: Bienenwelt -->
  <h2 class="abs" style="left:486px;top:25px;font-family:Merriweather,serif;font-weight:900;font-size:23px;line-height:31px;white-space:nowrap"><span style="color:var(--honey)">Faszinierende</span><br><span style="color:var(--forest)">Bienenwelt</span></h2>
  <p class="abs" style="left:485px;top:91px;font-family:Merriweather,serif;font-weight:700;font-size:11px;line-height:12.5px;color:var(--forest)">Wuss-<br>ten Sie<br>schon?</p>
  <div class="fill frame" role="img" aria-label="Foto: dicht gedrängte Bienen auf der Wabe" style="left:529px;top:91px;width:155px;height:130px;border-right:0;background:linear-gradient(135deg,#3b2a18,#a8743a 50%,#5a3e22);clip-path:polygon(0 0,100% 0,100% 100%,10% 100%,0 88%)"></div>
  <p class="abs body" style="left:486px;top:135px">Bienen<br>sind echte<br>Vielflieger!<br>Für Ihr<br>500g-Glas<br>Honig<br>legen<br>sie eine</p>
  <p class="abs body" style="left:486px;top:232px">Flugstrecke hin, die dreimal um die Erde reicht.</p>
  <p class="abs body" style="left:486px;top:249px">Sie verschenken ihr Lebenswerk! Eine Biene<br>produziert in ihrem ganzen Leben nur etwa<br>einen halben Teelöffel Honig. Genießen Sie den<br>Honig bewusst – es steckt viel Arbeit drin!</p>
  <p class="abs body" style="left:486px;top:302px">Im Bienenstock regiert eine knallharte Chefin!</p>
  <p class="abs body" style="left:584px;top:315px">Im Sommer legt<br>die Königin bis zu<br>2.000 Eier pro Tag.</p>
  <div class="fill honeycomb" role="img" aria-label="Wabenmuster" style="left:421px;top:374px;width:263px;height:110px;clip-path:polygon(0 70%,70% 0,100% 0,100% 100%,5% 100%)"></div>
  <div class="fill" role="img" aria-label="Foto: gestapelte Gläser Blütenhonig mit Etikett" style="left:427px;top:324px;width:150px;height:125px;background:linear-gradient(160deg,#f2b233,#c96a12 60%,#7a2a14);clip-path:polygon(20% 0,80% 0,85% 40%,100% 50%,95% 100%,25% 100%,0 70%,5% 40%,20% 35%)"></div>
</section>

</body>
</html>
```